e-Book Cover Design Project

I need an e-book cover design for a book called The Quiet Harbor. A fieldbook for hearts (run dry). It is non-fiction. It has an apple theme throughout so I would like to see designs that use a red apple (perhaps even a bite out of it), simple text and simple background. Despite the theme, the final design should still be positive.

Target Market(s)

Most likely women aged 25 and over.

Requirements
Must have
• real red apple
Nice to have
• cupids arrow
Should not have
• cartoons

```html
<!DOCTYPE html>
<html lang="en">
<head>
<meta charset="utf-8">
<title>The Quiet Harbor – eBook Cover</title>
<link rel="stylesheet" href="https://fonts.googleapis.com/css2?family=Bebas+Neue&family=Didact+Gothic&display=swap">
<style>
  :root {
    --brand-red: #d13b2c;
    --paper: #ffffff;
    --photo-red: #e0433a;
    --photo-red-soft: #ef8a80;
    --photo-grey: #8c8c8c;
    --photo-grey-soft: #c4c4c4;
  }
  html, body {
    margin: 0;
    padding: 0;
    overflow: hidden;
    background: var(--paper);
  }
  .cover {
    position: relative;
    width: 841px;
    height: 1200px;
    background: var(--paper);
    overflow: hidden;
  }
  .cover__header {
    position: absolute;
    left: 0;
    top: 0;
    width: 841px;
    height: 300px;
  }
  .title-text {
    font-family: "Bebas Neue", "Oswald", sans-serif;
    font-size: 116px;
    fill: var(--brand-red);
  }
  .subtitle-band { fill: var(--brand-red); }
  .subtitle-text {
    font-family: "Didact Gothic", "Quicksand", sans-serif;
    font-size: 36px;
    fill: var(--paper);
  }
  .cover__photo {
    position: absolute;
    left: 185px;
    top: 448px;
    width: 472px;
    height: 488px;
    background:
      linear-gradient(180deg, rgba(255,255,255,0.35) 0%, rgba(255,255,255,0) 30%, rgba(255,255,255,0) 85%, rgba(255,255,255,0.45) 100%),
      linear-gradient(90deg, var(--photo-red-soft) 0%, var(--photo-red) 22%, var(--photo-red) 44%, var(--photo-grey) 56%, var(--photo-grey) 80%, var(--photo-grey-soft) 100%);
  }
  .cover__author-band {
    position: absolute;
    left: 0;
    top: 1057px;
    width: 841px;
    height: 143px;
    background: var(--brand-red);
    display: flex;
    align-items: center;
    justify-content: center;
  }
  .author-name {
    font-family: "Bebas Neue", "Oswald", sans-serif;
    font-size: 140px;
    line-height: 1;
    letter-spacing: 4px;
    color: var(--paper);
    padding-top: 12px;
  }
</style>
</head>
<body>
  <main class="cover">
    <svg class="cover__header" viewBox="0 0 841 300" aria-label="The Quiet Harbor. A fieldbook for hearts (run dry)">
      <text class="title-text" x="43" y="152" textLength="738" lengthAdjust="spacing">THE QUIET HARBOR</text>

      <polygon class="subtitle-band"
        points="28,173 578,173 570,181 580,188 568,196 578,203 569,211 577,222 28,222"/>
      <text class="subtitle-text" x="40" y="209" textLength="520" lengthAdjust="spacing">A fieldbook for hearts</text>

      <g transform="rotate(11 585 180)">
        <polygon class="subtitle-band"
          points="585,176 802,176 802,226 586,226 578,216 587,208 577,199 586,192 578,184"/>
        <text class="subtitle-text" x="606" y="212" textLength="176" lengthAdjust="spacing">run dry</text>
      </g>
    </svg>

    <div class="cover__photo" role="img" aria-label="Photograph of a real red apple, left half in full colour and right half in greyscale"></div>

    <footer class="cover__author-band">
      <span class="author-name">AUTHOR</span>
    </footer>
  </main>
</body>
</html>
```